Post Card (5x7) - Pre-foreclosure Image - Harbor Path Partners

(Two-Sided Post Card)
FACING FORECLOSURE? YOU STILL HAVE OPTIONS.
If you’re behind on payments or at risk of foreclosure, you’re not alone—and it’s not too late to take action.
We help homeowners:
• Explore options to stay in their home
• Stop or delay foreclosure
• Sell quickly for a fair price if needed
No pressure. No obligation. Just real solutions tailored to your situation.
Call - (240) 558-2094
Email - marcus@hpbllc-mail.com
Harbor Path Partners LLC
7200 Bramwick Lane, Ellicott City, MD 21043
**Marcus Fennimore is a Licensed Realtor with Copperleaf Homes Realty in Bethesda, Maryland.
(Leave room for mailing address, return address & postage)
Target Market(s)
Distressed Homeowners
Industry/Entity Type
Real Estate

```html
<!DOCTYPE html>
<html lang="en">
<head>
<meta charset="utf-8">
<title>Harbor Path Partners – Pre-foreclosure Postcard</title>
<link rel="stylesheet" href="https://fonts.googleapis.com/css2?family=Bebas+Neue&family=Montserrat:wght@800&family=Poppins:wght@400;500&display=swap">
<style>
:root{
  --backdrop:#545454;
  --paper:#ffffff;
  --gold:#b0890a;
  --ink:#000000;
  --grey:#8c8c8c;
  --rule:#c9c9c9;
}
*{margin:0;padding:0;box-sizing:border-box}
html,body{width:863px;height:1200px;overflow:hidden;background:var(--backdrop)}
.card{position:absolute;left:105px;width:653px;height:466px;background:var(--paper);overflow:hidden}
.card--front{top:100px}
.card--back{top:633px}
.abs{position:absolute;white-space:nowrap}
.display{font-family:'Bebas Neue',Impact,sans-serif;line-height:.9}
.heavy{font-family:'Montserrat',Arial,sans-serif;font-weight:800;line-height:1}
.body{font-family:'Poppins',Arial,sans-serif}
.gold{color:var(--gold)}
.ink{color:var(--ink)}

.headline-facing{left:35px;top:26px;font-size:75px;letter-spacing:-1px}
.headline-foreclosure{left:35px;top:93px;font-size:69px}
.headline-options{left:37px;top:154px;font-size:23px;letter-spacing:-.2px}
.lede{left:37px;top:188px;font-size:11px;line-height:13.5px;color:var(--grey)}

.benefits{position:absolute;left:33px;top:229px;width:169px;list-style:none}
.benefits li{height:36.3px;display:flex;align-items:flex-start;padding:4px 4px 0 7px;color:#fff;font-family:'Poppins',Arial,sans-serif;font-weight:500;font-size:13px;line-height:14px;white-space:nowrap}
.benefits li:nth-child(odd){background:var(--gold)}
.benefits li:nth-child(even){background:var(--ink)}
.benefits svg{flex:none;width:11px;height:11px;margin:2px 3px 0 0}

.photo{position:absolute}
.photo--sign-small{left:205px;top:229px;width:70px;height:109px;background:linear-gradient(180deg,#3f77b5 0%,#d4d8de 30%,#c9242b 45%,#c9242b 75%,#5e7b3c 100%)}

.cta{left:37px;font-size:24px;letter-spacing:.2px}
.phone{left:37px;font-size:51px;color:var(--ink)}
.contacts{left:37px;display:flex;gap:7px;font-size:9px;letter-spacing:-.2px;font-weight:500;color:var(--ink);align-items:center}
.contacts span{display:flex;align-items:center;gap:4px}
.contacts svg{width:11px;height:11px}

.shapes{position:absolute;left:0;top:0}
.brand-front{left:372px;width:262px;top:178px;text-align:center;color:#fff;font-family:'Poppins',Arial,sans-serif;font-weight:500;font-size:12px;letter-spacing:2px}

/* back */
.back-real{left:34px;top:25px;font-size:50px}
.back-nopress{left:34px;top:64px;font-size:50px}
.back-lede{left:34px;top:110px;font-size:11px;line-height:13.5px;color:var(--grey)}
.back-list{left:34px;font-size:50px}
.licence{left:38px;top:297px;font-size:11px;line-height:13.5px;color:var(--grey)}
.street{left:40px;top:341px;font-size:11px;font-weight:500;color:var(--ink)}
.stamp{position:absolute;left:523px;top:31px;width:95px;height:95px;border:1px solid var(--rule)}
.address-line{position:absolute;left:437px;width:180px;height:1px;background:var(--rule)}
.return{right:36px;top:241px;text-align:right;font-size:11px;line-height:12.5px;color:var(--grey);font-weight:500}
.brand-back{left:500px;top:420px;width:125px;text-align:center;font-family:'Poppins',Arial,sans-serif;font-weight:500;font-size:10px;letter-spacing:1px;color:var(--ink);white-space:normal;line-height:12px}
</style>
</head>
<body>

<section class="card card--front">
  <svg class="shapes" width="653" height="466" viewBox="0 0 653 466">
    <defs>
      <linearGradient id="sunset" x1="0" y1="0" x2="0" y2="1">
        <stop offset="0" stop-color="#6d7a8c"/>
        <stop offset=".45" stop-color="#c98a3c"/>
        <stop offset=".7" stop-color="#2a2420"/>
        <stop offset="1" stop-color="#8c5a2c"/>
      </linearGradient>
      <linearGradient id="harbor" x1="0" y1="0" x2="0" y2="1">
        <stop offset="0" stop-color="#8a7aa0"/>
        <stop offset=".4" stop-color="#b9869a"/>
        <stop offset=".75" stop-color="#a05a3a"/>
        <stop offset="1" stop-color="#6e5866"/>
      </linearGradient>
    </defs>
    <polygon points="372,0 633,0 633,193 502,267 372,193" fill="var(--gold)"/>
    <polygon points="390,0 614,0 614,183 502,246 390,183" fill="url(#sunset)" role="img" aria-label="City skyline silhouetted at sunset over water"/>
    <polygon points="296,466 296,309 426,234 502,277 577,234 653,277 653,466" fill="var(--ink)"/>
    <polygon points="315,466 315,318 426,255 502,298 577,255 653,298 653,466" fill="url(#harbor)" role="img" aria-label="Harbor waterfront skyline at dusk"/>
  </svg>
  <div class="abs brand-front">HARBOR PATH PARTNERS LLC</div>

  <h1>
    <span class="abs heavy gold headline-facing">FACING</span>
    <span class="abs display ink headline-foreclosure">FORECLOSURE?</span>
  </h1>
  <h2 class="abs heavy gold headline-options">YOU STILL HAVE OPTIONS</h2>
  <p class="abs body lede">If you’re behind on payments or at risk of foreclosure,<br>you’re not alone—and it’s not too late to take action.</p>

  <ul class="benefits">
    <li><svg viewBox="0 0 12 12"><circle cx="6" cy="6" r="5" fill="none" stroke="#fff" stroke-width="1.3"/><path d="M3.5 6.2l1.7 1.6 3.3-3.4" fill="none" stroke="#fff" stroke-width="1.3"/></svg><span>Explore options<br>to stay in their home</span></li>
    <li><svg viewBox="0 0 12 12"><circle cx="6" cy="6" r="5" fill="none" stroke="#fff" stroke-width="1.3"/><path d="M3.5 6.2l1.7 1.6 3.3-3.4" fill="none" stroke="#fff" stroke-width="1.3"/></svg><span>Stop or delay<br>foreclosure</span></li>
    <li><svg viewBox="0 0 12 12"><circle cx="6" cy="6" r="5" fill="none" stroke="#fff" stroke-width="1.3"/><path d="M3.5 6.2l1.7 1.6 3.3-3.4" fill="none" stroke="#fff" stroke-width="1.3"/></svg><span>Sell quickly for a<br>fair price if needed</span></li>
  </ul>
  <div class="photo photo--sign-small" role="img" aria-label="Foreclosure for-sale sign in front of a house"></div>

  <p class="abs heavy gold cta" style="top:356px">CALL NOW TODAY!</p>
  <p class="abs display phone" style="top:385px">(240) 558-2094</p>
  <p class="abs body contacts" style="top:428px">
    <span><svg viewBox="0 0 12 12"><circle cx="6" cy="6" r="5" fill="none" stroke="var(--gold)" stroke-width="1.2"/><ellipse cx="6" cy="6" rx="2.2" ry="5" fill="none" stroke="var(--gold)" stroke-width="1"/><path d="M1 6h10" stroke="var(--gold)" stroke-width="1"/></svg>www.hpbllc-mail.com</span>
    <span><svg viewBox="0 0 12 12"><rect x="1" y="2.5" width="10" height="7" rx="1" fill="none" stroke="var(--gold)" stroke-width="1.2"/><path d="M1.5 3l4.5 3.5L10.5 3" fill="none" stroke="var(--gold)" stroke-width="1.2"/></svg>marcus@hpbllc-mail.com</span>
  </p>
</section>

<section class="card card--back">
  <h2>
    <span class="abs display gold back-real">REAL SOLUTIONS.</span>
    <span class="abs display ink back-nopress">NO PRESSURE.</span>
  </h2>
  <p class="abs body back-lede">We understand how overwhelming foreclosure can feel.<br>Our team works directly with homeowners to provide<br>real, practical solutions tailored to your situation.</p>
  <p class="abs display gold back-list" style="top:155px">NO PRESSURE.</p>
  <p class="abs display gold back-list" style="top:194px">NO OBLIGATION.</p>
  <p class="abs display ink back-list" style="top:233px">JUST HONEST GUIDANCE.</p>

  <p class="abs body licence">Marcus Fennimore is a Licensed Realtor with<br>Copperleaf Homes Realty in Bethesda, Maryland.</p>
  <p class="abs body street">7200 Bramwick Lane Ellicott City, MD 21043</p>
  <p class="abs heavy gold cta" style="top:357px">CALL NOW TODAY!</p>
  <p class="abs display phone" style="top:385px">(240) 558-2094</p>
  <p class="abs body contacts" style="top:428px">
    <span><svg viewBox="0 0 12 12"><circle cx="6" cy="6" r="5" fill="none" stroke="var(--gold)" stroke-width="1.2"/><ellipse cx="6" cy="6" rx="2.2" ry="5" fill="none" stroke="var(--gold)" stroke-width="1"/><path d="M1 6h10" stroke="var(--gold)" stroke-width="1"/></svg>www.hpbllc-mail.com</span>
    <span><svg viewBox="0 0 12 12"><rect x="1" y="2.5" width="10" height="7" rx="1" fill="none" stroke="var(--gold)" stroke-width="1.2"/><path d="M1.5 3l4.5 3.5L10.5 3" fill="none" stroke="var(--gold)" stroke-width="1.2"/></svg>marcus@hpbllc-mail.com</span>
  </p>

  <svg class="shapes" width="653" height="466" viewBox="0 0 653 466" style="pointer-events:none">
    <defs>
      <linearGradient id="house" x1="0" y1="0" x2="0" y2="1">
        <stop offset="0" stop-color="#c8ccd2"/>
        <stop offset=".35" stop-color="#8a7f76"/>
        <stop offset=".5" stop-color="#c9242b"/>
        <stop offset=".78" stop-color="#c9242b"/>
        <stop offset="1" stop-color="#e4e2de"/>
      </linearGradient>
    </defs>
    <polygon points="294,466 294,342 374,298 453,342 453,466" fill="var(--gold)"/>
    <polygon points="306,466 306,352 374,314 442,352 442,466" fill="url(#house)" role="img" aria-label="Foreclosure for-sale sign in front of a snowy house"/>
  </svg>

  <div class="stamp" aria-label="Postage"></div>
  <div class="address-line" style="top:156px"></div>
  <div class="address-line" style="top:190px"></div>
  <div class="address-line" style="top:224px"></div>
  <p class="abs body return">7200 Bramwick Lane<br>Ellicott City, MD 21043</p>
  <p class="abs brand-back">HARBOR PATH<br>PARTNERS LLC</p>
</section>

</body>
</html>
```